***Design a Nutritional Supplement Label for Bright Harvest!***

I have an existing label, I want to keep the logo but change the rest of the design. I am open to different creative ideas, but it needs to look appropriate for the shelves at Bright Harvest. This means it needs to look professional and premium, without being sterile and boring. I feel like my current label looks a little 1990s. You can play with the colors, font and design elements, while keeping the logo, descriptive text and the same layout. Feel free to take some bold chances. (You cannot change the font in the supplement facts section)

Font styles to use
Sans Serif

Colors

Designer to choose colors to be used in the design.

Requirements
Must have
• Keep the same text and layout. Keep the "Muscle Haven" logo as-is. DO NOT CHANGE THE LOGO!!

```html
<!DOCTYPE html>
<html lang="en">
<head>
<meta charset="utf-8">
<title>Muscle Haven – Supplement Label</title>
<link href="https://fonts.googleapis.com/css2?family=Lato:wght@400;700;900&family=Roboto+Condensed:wght@400;700&family=Saira+Condensed:wght@800&display=swap" rel="stylesheet">
<style>
  :root{
    --page:#3b3b3d;
    --white:#ffffff;
    --ink:#1d1d1f;
    --black:#121212;
    --brand-blue:#3d9ad6;
    --brand-blue-deep:#1f78c1;
    --brand-green:#97c13c;
    --sky:#cfe6f5;
    --muted:#3a3a3a;
  }
  *{box-sizing:border-box;margin:0;padding:0}
  html,body{width:924px;height:1200px;overflow:hidden;background:var(--page)}
  .label{
    position:absolute;left:67px;top:438px;width:790px;height:324px;
    background:var(--white);overflow:hidden;
    box-shadow:0 8px 18px rgba(0,0,0,.45);
    font-family:"Lato",sans-serif;color:var(--ink);
  }
  .label-bg{position:absolute;inset:0}
  .copy{position:absolute;font-size:8.2px;line-height:10.4px;text-align:justify}
  .copy--intro{left:16px;top:26px;width:228px}
  .copy--note{left:16px;top:190px;width:228px;background:rgba(255,255,255,.88);padding:3px 4px;text-align:left;font-size:7.8px;line-height:10px}
  .blank-box{position:absolute;left:16px;top:128px;width:228px;height:50px;border:1.3px solid var(--ink);background:var(--white)}
  .barcode-slot{position:absolute;left:48px;top:250px;width:150px;height:64px;background:var(--white);
    display:flex;align-items:center;justify-content:center;font-size:18px;color:var(--muted)}
  .brand{position:absolute;left:262px;top:26px;width:272px;text-align:center;color:var(--brand-blue);font-weight:900}
  .brand__top{display:block;font-size:58px;line-height:60px;letter-spacing:1px}
  .brand__bottom{display:block;font-size:30px;line-height:36px;letter-spacing:18px;padding-left:18px}
  .claim{position:absolute;left:252px;top:150px;width:284px;height:134px}
  .count{position:absolute;left:294px;top:280px;width:200px;text-align:center;color:var(--white);
    font-weight:700;font-size:12.5px;line-height:15.5px}
  .facts{position:absolute;left:566px;top:22px;width:198px;border:1.6px solid var(--ink);padding:2px 4px;
    font-family:"Roboto Condensed",sans-serif;background:var(--white)}
  .facts__title{font-weight:700;font-size:23px;line-height:24px;letter-spacing:-.3px;border-bottom:1px solid var(--ink)}
  .facts__row{display:flex;justify-content:space-between;font-size:8px;line-height:11px}
  .facts__row--serving{border-bottom:5px solid var(--ink);padding:1px 0}
  .facts__row--head{font-weight:700;border-bottom:1px solid var(--ink);padding:2px 0}
  .facts__nutrient{font-size:8px;line-height:9px;padding:2px 0 1px;border-bottom:4px solid var(--ink)}
  .facts__nutrient small{display:block;font-size:6.6px;line-height:8px}
  .facts__foot{font-size:7.6px;padding-top:2px}
  .maker{position:absolute;left:588px;top:196px;width:162px;text-align:center;color:var(--white);
    font-family:"Roboto Condensed",sans-serif;font-weight:700;font-size:8.4px;line-height:10.6px}
  .free-from{position:absolute;left:586px;top:242px;width:166px;border-top:1.2px solid var(--white);border-bottom:1.2px solid var(--white);
    text-align:center;color:var(--white);font-family:"Roboto Condensed",sans-serif;font-weight:700;font-size:6.6px;line-height:8.6px;padding:1px 0}
  .storage{position:absolute;left:608px;top:266px;width:116px;text-align:center;color:var(--white);font-family:"Roboto Condensed",sans-serif;font-weight:700}
  .storage__note{font-size:7.4px;line-height:9px}
  .storage__recycle{font-size:11.5px;line-height:13px;letter-spacing:.2px}
  .seal{position:absolute;top:265px;width:28px;height:28px;border-radius:50%;background:var(--white)}
  .seal--left{left:594px}.seal--right{left:710px}
  .trademark{position:absolute;left:560px;top:298px;width:220px;text-align:center;color:var(--white);
    font-family:"Roboto Condensed",sans-serif;font-weight:700;font-size:6.4px}
</style>
</head>
<body>
<main class="label">
  <svg class="label-bg" width="790" height="324" viewBox="0 0 790 324" aria-hidden="true">
    <defs>
      <linearGradient id="sky" x1="0" y1="0" x2="0" y2="1">
        <stop offset="0" stop-color="#ffffff"/>
        <stop offset="1" stop-color="#bcdcf2"/>
      </linearGradient>
    </defs>
    <rect width="790" height="324" fill="#ffffff"/>
    <rect y="140" width="790" height="184" fill="url(#sky)"/>
    <path d="M0 150 C70 160 150 205 300 232 L300 252 C150 232 70 190 0 176 Z" fill="var(--brand-blue)"/>
    <path d="M0 172 C80 186 160 226 310 246 L310 256 C160 240 80 202 0 188 Z" fill="var(--brand-green)"/>
    <path d="M0 238 C150 244 300 262 400 256 C520 250 600 184 790 166 L790 178 C610 196 520 262 400 268 C300 274 150 256 0 252 Z" fill="var(--brand-green)"/>
    <path d="M0 250 C150 254 300 272 400 266 C520 260 600 194 790 176 L790 324 L0 324 Z" fill="var(--black)"/>
  </svg>

  <p class="copy copy--intro">Lorem ipsum dolor sit amet, consectetuer adipiscing elit, sed diam nonummy nibh euismod tincidunt ut laoreet dolore magna aliquam erat volutpat. Ut wisi enim ad minim veniam, quis nostrud exerci tation ullamcorper suscipit lobortis nisl ut aliquip ex ea commodo consequat. Duis autem vel eum iriure dolor in hendrerit in vulputate velit esse molestie consequat, vel illum dolore eu feugiat nulla facilisis at vero eros et accumsan et iusto odio dignissim qui blandit praesent luptatum zzril delenit augue duis dolore te feugait nulla facilisi.</p>
  <div class="blank-box"></div>
  <p class="copy copy--note">Lorem ipsum dolor sit amet, consectetuer adipiscing elit, sed diam nonummy nibh euismod tincidunt ut laoreet dolore magna aliquam erat volutpat. Ut wisi enim ad minim veniam, quis nostrud exerci tation ullamcorper suscipit lobortis nisl ut aliquip ex ea commodo consequat.</p>
  <div class="barcode-slot">bar code</div>

  <h1 class="brand"><span class="brand__top">MUSCLE</span><span class="brand__bottom">HAVEN</span></h1>

  <svg class="claim" viewBox="0 0 284 134" aria-label="High absorption, fast acting">
    <polygon points="40,34 262,4 252,46 30,72" fill="var(--brand-green)"/>
    <polygon points="20,64 280,28 262,100 4,130" fill="var(--brand-blue-deep)"/>
    <polygon points="28,66 272,34 256,94 12,122" fill="var(--brand-blue)"/>
    <g font-family="'Saira Condensed',sans-serif" font-weight="800" fill="#ffffff">
      <text x="0" y="0" font-size="24" transform="translate(60,56) rotate(-7) skewX(-14)">HIGH ABSORPTION</text>
      <text x="0" y="0" font-size="46" transform="translate(34,112) rotate(-9) skewX(-14)">FAST ACTING</text>
    </g>
  </svg>

  <p class="count">180 CAPSULES<br>DIETARY SUPPLEMENT</p>

  <section class="facts">
    <h2 class="facts__title">Supplement Facts</h2>
    <div class="facts__row facts__row--serving"><span>Serving Size: 1 Capsule</span><span>Servings Per Container: 180</span></div>
    <div class="facts__row facts__row--head"><span>Amount Per Serving</span><span>% Daily Value</span></div>
    <div class="facts__nutrient">
      <div class="facts__row"><span>Magnesium</span><span>70 mg&nbsp;&nbsp;17%</span></div>
      <small>Fully-reacted magnesium malate complex (Magnora®)</small>
    </div>
    <p class="facts__foot">*Daily Value not established.</p>
  </section>

  <p class="maker">Produced for and distributed by<br>Northvale Labs LLC., Denver, CO 80205<br>support@musclehaven.example<br>www.musclehaven.example</p>
  <p class="free-from">This product contains no salt, starch, yeast, wheat,<br>gluten, corn, soy, milk, egg, shellfish or preservatives.</p>
  <span class="seal seal--left"></span>
  <div class="storage"><p class="storage__note">Store in a cool dry place.</p><p class="storage__recycle">PLEASE RECYCLE.</p></div>
  <span class="seal seal--right"></span>
  <p class="trademark">Magnora® and Muscle Haven® are registered trademarks of Northvale Labs LLC.</p>
</main>
</body>
</html>
```